Project Report for American Indian and Alaska Native org (U.S.)

We need a report formatted/ design / layout.
We are a nonprofit organization that works on indigenous elder issues.
The report should reflect our logo color scheme.
Body font should be at least 11 point sans serif.
Ideally, headings and title would use fonts that are reminiscent of tribal cultures though not hard to read or whimsical/ unprofessional looking.

We have used some light script style fonts in the past -- nothing too cursive looking though.

The audience is public health professionals and tribal staff and leadership.

We want our organization's logo (QV7) and the project logo (brain health) incorporated into the title page.

We prefer the files to come back to us in an editable fashion + a pdf file.

Industry/Entity Type

tribal communities and public health officials

Font styles to use
Serif
Sans Serif

Requirements
Must have
• our logo and color scheme
Should not have
• headdress images

```html
<!DOCTYPE html>
<html lang="en">
<head>
<meta charset="utf-8">
<title>Tribal Law and Policy Regarding Alzheimer's Disease and Related Dementia Issues</title>
<link rel="stylesheet" href="https://fonts.googleapis.com/css2?family=Staatliches&family=Arimo:wght@400&display=swap">
<style>
  :root {
    --teal: #56a7b1;
    --rust: #ad5a4f;
    --ink: #1a1a1a;
    --paper: #ffffff;
    --shadow: #111111;
  }
  html, body {
    margin: 0;
    padding: 0;
    overflow: hidden;
  }
  .spread {
    position: relative;
    width: 1200px;
    height: 424px;
    background: var(--paper);
    overflow: hidden;
    font-family: "Arimo", Arial, sans-serif;
    color: var(--ink);
  }

  /* Contents page */
  .contents-tab {
    position: absolute;
    left: 0;
    top: 43px;
    width: 171px;
    height: 53px;
    background: linear-gradient(to bottom, var(--teal), var(--rust));
  }
  .contents-tab h2 {
    margin: 0;
    position: absolute;
    left: 34px;
    top: 11px;
    font-family: "Staatliches", Impact, sans-serif;
    font-weight: 400;
    font-size: 24px;
    letter-spacing: 1px;
    color: var(--paper);
    line-height: 1;
  }
  .rule-top {
    position: absolute;
    left: 172px;
    top: 49px;
    width: 376px;
    height: 2px;
    background: var(--rust);
  }
  .rule-side {
    position: absolute;
    left: 139px;
    top: 98px;
    width: 2px;
    height: 247px;
    background: var(--rust);
  }
  .contents-frame {
    position: absolute;
    left: 144px;
    top: 55px;
    width: 405px;
    height: 291px;
    border: 2px solid var(--teal);
  }
  .toc {
    position: absolute;
    left: 189px;
    top: 60px;
    width: 343px;
    margin: 0;
    padding: 0;
    list-style: none;
    font-size: 8px;
    line-height: 15.15px;
  }
  .toc li {
    display: flex;
    align-items: baseline;
  }
  .toc .level-2 { padding-left: 20px; }
  .toc .level-3 { padding-left: 40px; }
  .toc .title { white-space: nowrap; }
  .toc .title.wrap { white-space: normal; }
  .toc .leader {
    flex: 1;
    margin: 0 2px;
    border-bottom: 1px dotted #555;
    transform: translateY(-2px);
  }
  .toc .page { white-space: nowrap; }
  .toc .wrapped {
    display: block;
  }
  .toc .wrapped .line-end {
    display: flex;
    align-items: baseline;
  }

  /* Title page */
  .cover {
    position: absolute;
    left: 600px;
    top: 0;
    width: 600px;
    height: 424px;
    background: linear-gradient(to bottom, #58a8b2 0%, #8b8580 45%, #ad5a4f 100%);
  }
  .pattern-band {
    position: absolute;
    left: 0;
    width: 600px;
    height: 20px;
  }
  .pattern-band.upper { top: 44px; background: rgba(173, 90, 79, 0.55); }
  .pattern-band.lower { top: 324px; background: rgba(86, 167, 177, 0.55); }
  .cover-title {
    position: absolute;
    left: 0;
    top: 115px;
    width: 600px;
    margin: 0;
    text-align: center;
    font-family: "Staatliches", Impact, sans-serif;
    font-weight: 400;
    font-size: 33px;
    line-height: 42.7px;
    letter-spacing: 0.5px;
    color: var(--paper);
    text-shadow: 2px 2px 0 var(--shadow);
  }
  .cover-title span { display: block; }
</style>
</head>
<body>
<main class="spread">
  <section class="contents-page">
    <div class="contents-tab"><h2>Contents</h2></div>
    <div class="rule-top"></div>
    <div class="rule-side"></div>
    <div class="contents-frame"></div>
    <ol class="toc">
      <li><span class="title">Executive Summary</span><span class="leader"></span><span class="page">4</span></li>
      <li><span class="title">Background</span><span class="leader"></span><span class="page">5</span></li>
      <li class="level-2"><span class="title">Road Map for Indian Country</span><span class="leader"></span><span class="page">6</span></li>
      <li class="level-2"><span class="title">Tribal Sovereignty</span><span class="leader"></span><span class="page">7</span></li>
      <li><span class="title">Process</span><span class="leader"></span><span class="page">7</span></li>
      <li class="level-2"><span class="title">Primary Sources</span><span class="leader"></span><span class="page">7</span></li>
      <li class="level-2"><span class="title">Secondary Sources</span><span class="leader"></span><span class="page">7</span></li>
      <li class="level-3"><span class="title">Road Map Development and Subsequent Activities</span><span class="leader"></span><span class="page">7</span></li>
      <li class="level-3"><span class="title">Model Statute Council</span><span class="leader"></span><span class="page">7</span></li>
      <li class="level-3 wrapped">
        <span class="title">Assembly of State Lawmakers (Circle of Native State</span>
        <span class="line-end"><span class="title">Legislators)</span><span class="leader"></span><span class="page">7</span></span>
      </li>
      <li><span class="title">Results</span><span class="leader"></span><span class="page">8</span></li>
      <li><span class="title">Related Policy Issues Collections</span><span class="leader"></span><span class="page">8</span></li>
      <li><span class="title">State Alzheimer Plans</span><span class="leader"></span><span class="page">9</span></li>
      <li><span class="title">National Plan to Address Alzheimer's Disease</span><span class="leader"></span><span class="page">11</span></li>
      <li><span class="title">Other National Plans</span><span class="leader"></span><span class="page">11</span></li>
      <li><span class="title">Conclusion</span><span class="leader"></span><span class="page">11</span></li>
      <li><span class="title">Citations</span><span class="leader"></span><span class="page">12</span></li>
    </ol>
  </section>

  <section class="cover">
    <div class="pattern-band upper" role="img" aria-label="Decorative band of repeating diamond motifs in rust"></div>
    <h1 class="cover-title">
      <span>Tribal Law and Policy</span>
      <span>Regarding Alzheimer's Disease</span>
      <span>and</span>
      <span>Related Dementia Issues</span>
    </h1>
    <div class="pattern-band lower" role="img" aria-label="Decorative band of repeating diamond motifs in teal"></div>
  </section>
</main>
</body>
</html>
```